QRV Advisors needs a web site

We need a web site for www.qrvadvisors-example.com. QRV is a mergers and acquisition consulting company that focuses our buyer and seller services on logistics companies. We help put companies together, and help with legal and financial due diligence. We want the web site to express our service and show the logistics components. We want personalized images versus pictures of trucks and airplanes.

Our new logo uses Burgandy and grey colors. Image attached. We are not in to bold, big letters...classy, artistic, low key preferred. Confidentiality, experience, professional are what we want to express on the site.

All we expect for the first part of this project is a home page, and one subpage.  We are budgeting other funds for the technical aspects of the web site

Reason: All that I'm seeing so far is trucks, forklifts and planes. We are a legal mergers and acquisitions firm that focus on logistics. I like some of the images to say logistics, but really want it say legal, financial, and putting companies together. Will pay extra for the sub page if someone can impress us with a home page.

Reason: Swamped with another project at the moment...will work on this over the weekend and provide designer feedback and select final design by Tuesday

```html
<!DOCTYPE html>
<html lang="en">
<head>
<meta charset="utf-8">
<title>QRV Advisors</title>
<link href="https://fonts.googleapis.com/css2?family=Arimo:ital,wght@0,400;0,700;1,400;1,700&family=Roboto+Condensed:wght@300;400;700&display=swap" rel="stylesheet">
<style>
:root{
  --burgundy:#a6093d;
  --charcoal:#231f20;
  --black:#0c0c0c;
  --white:#ffffff;
  --ink:#1a1a1a;
  --muted:#8a8a8a;
}
*{margin:0;padding:0;box-sizing:border-box}
html,body{width:760px;height:1200px;overflow:hidden;background:var(--white)}
body{position:relative;font-family:"Arimo",Arial,sans-serif;color:var(--ink)}
.abs{position:absolute}
.cond{font-family:"Roboto Condensed","Arial Narrow",sans-serif}

/* header */
.top-strip{left:0;top:0;width:760px;height:5px;background:var(--burgundy)}
.header{left:0;top:5px;width:760px;height:106px;background:var(--charcoal)}
.brand{left:92px;top:40px;color:var(--white)}
.brand-name{font-family:"Roboto Condensed",sans-serif;font-weight:300;font-size:50px;letter-spacing:10px;line-height:50px}
.brand-tag{font-size:6px;color:var(--burgundy);margin-top:2px;letter-spacing:.2px}
.search{left:557px;top:20px;width:87px;height:19px;background:var(--white);font-size:8px;color:#aaa;padding:5px 5px}
.search-btn{left:644px;top:20px;width:21px;height:19px;background:var(--burgundy)}
.nav{left:297px;top:62px;width:370px;height:26px;background:var(--burgundy);display:flex;align-items:center;justify-content:space-around;padding:0 4px}
.nav a{font-family:"Roboto Condensed",sans-serif;font-size:7.5px;color:var(--white);text-decoration:none;position:relative}
.nav a.active::after{content:"";position:absolute;left:-6px;right:-6px;bottom:-6px;height:2px;background:var(--white)}

/* hero */
.hero{left:0;top:111px;width:760px;height:262px;
  background:linear-gradient(100deg,#f7c77a 0%,#f2a24a 22%,#e98a3c 38%,#b9a6a0 58%,#8d98ad 75%,#c6b7b2 100%)}
.hero-title{left:116px;top:207px;font-family:"Roboto Condensed",sans-serif;font-weight:300;font-size:35px;line-height:41px;color:var(--burgundy)}
.hero-text{left:117px;top:292px;font-size:9.5px;line-height:14px;color:var(--ink)}
.arrow{top:228px}

/* welcome */
.welcome-title{left:0;top:385px;width:760px;text-align:center;font-family:"Roboto Condensed",sans-serif;font-size:22px;letter-spacing:.5px}
.welcome-text{left:118px;top:424px;width:524px;text-align:center;font-size:8.3px;line-height:13.5px}
.feature{top:488px;width:190px;text-align:center}
.feature-photo{width:134px;height:134px;border-radius:50%;border:7px solid var(--burgundy);margin:0 auto}
.feature h3{font-family:"Roboto Condensed",sans-serif;font-weight:700;font-size:11px;margin-top:18px}
.feature p{font-size:7.3px;line-height:11px;margin:6px auto 0;width:140px}
.more{display:inline-block;margin-top:10px;background:var(--black);color:var(--white);font-family:"Roboto Condensed",sans-serif;font-size:7px;width:53px;height:14px;line-height:14px}

/* services */
.services{left:0;top:738px;width:760px;height:196px;background:var(--burgundy)}
.services-title{left:0;top:752px;width:760px;text-align:center;font-family:"Roboto Condensed",sans-serif;font-weight:300;font-size:26px;color:var(--white)}
.service{top:806px;width:173px;height:103px;background:var(--white);box-shadow:0 7px 6px -3px rgba(0,0,0,.75)}
.service-photo{height:84px}
.service span{display:block;text-align:center;font-size:12.5px;line-height:19px;color:var(--ink)}

/* testimonial */
.testi-title{left:0;top:946px;width:760px;text-align:center;font-family:"Roboto Condensed",sans-serif;font-weight:300;font-size:22px}
.avatar{left:348px;top:982px;width:64px;height:64px;border-radius:50%;border:5px solid var(--charcoal);background:radial-gradient(circle at 50% 45%,#e9dcd2,#b8a89b 70%,#7d7069)}
.quote{left:184px;top:1062px;width:420px;font-style:italic;font-size:7.8px;line-height:12px}
.qmark{font-family:"Arimo",sans-serif;font-style:italic;font-weight:700;font-size:22px;line-height:22px;color:var(--charcoal)}
.author{left:480px;top:1094px;width:123px;text-align:right;font-style:italic;font-weight:700;font-size:10.5px;color:var(--burgundy)}

/* footer */
.footer-nav{left:0;top:1120px;width:760px;height:36px;background:var(--black)}
.footer-nav a{position:absolute;top:14px;font-size:7px;color:var(--white);text-decoration:none}
.footer-nav a.active::after{content:"";position:absolute;left:-4px;right:-4px;bottom:-6px;height:1px;background:var(--burgundy)}
.footer-bar{left:0;top:1156px;width:760px;height:44px;background:var(--charcoal)}
.copyright{left:0;top:1169px;width:760px;text-align:center;font-size:6.8px;color:var(--white)}
.social{top:1161px;width:18px;height:18px;border-radius:2px}
</style>
</head>
<body>
<div class="abs top-strip"></div>
<header class="abs header"></header>
<div class="abs brand">
  <div class="brand-name">QRV</div>
  <div class="brand-tag">Mergers &amp; Acquisitions Consulting Services</div>
</div>
<div class="abs search">SEARCH</div>
<div class="abs search-btn">
  <svg width="21" height="19" viewBox="0 0 21 19"><circle cx="9" cy="8" r="3.6" fill="none" stroke="#fff" stroke-width="1.6"/><line x1="11.6" y1="10.6" x2="15.5" y2="14.5" stroke="#fff" stroke-width="2"/></svg>
</div>
<nav class="abs nav">
  <a class="active">HOME</a><a>ABOUT US</a><a>SERVICES</a><a>OFFICE NETWORKS</a><a>CONTACT US</a><a>GENERAL INFO</a>
</nav>

<section class="abs hero" role="img" aria-label="Photo of a silver truck speeding along a highway at sunset"></section>
<h1 class="abs hero-title">LOREM IPSUM<br>DOLOR SIT AMET</h1>
<p class="abs hero-text">Lorem ipsum dolor sit amet, consectetur adipisicing<br>elit, sed do eiusmod tempor incididunt ut labore et dolore magna aliqua.</p>
<svg class="abs arrow" style="left:55px" width="24" height="24" viewBox="0 0 24 24"><polyline points="22,2 2,12 22,22" fill="none" stroke="#222" stroke-width="1"/></svg>
<svg class="abs arrow" style="left:686px" width="24" height="24" viewBox="0 0 24 24"><polyline points="2,2 22,12 2,22" fill="none" stroke="#222" stroke-width="1"/></svg>

<h2 class="abs welcome-title">WELCOME TO QRV</h2>
<p class="abs welcome-text">QRV assists business owners within the logistics industry to implement growth and exit strategies. We offer business planning and merger and acquisition(M&amp;A) advisory services. QRV services are offered by industry executives with extensive M&amp;A experience. Your company will benefit from a unique and outside perspective from consultants that understand your business.</p>

<div class="abs feature" style="left:88px">
  <div class="feature-photo" role="img" aria-label="Photo of a man working on a laptop at a desk" style="background:linear-gradient(135deg,#6a4a36,#3a5a84 55%,#2a2422)"></div>
  <h3>LOREM IPSUM DOLOR</h3>
  <p>Lorem ipsum dolor sit amet, consectetur adipisicing elit, sed do eiusmod tempor incididunt</p>
  <span class="more">READ MORE</span>
</div>
<div class="abs feature" style="left:280px">
  <div class="feature-photo" role="img" aria-label="Photo of a smiling courier holding a clipboard" style="background:linear-gradient(160deg,#cfe0c4,#7aa36a 45%,#1d2640 70%,#e27a3a)"></div>
  <h3>LOREM IPSUM DOLOR</h3>
  <p>Lorem ipsum dolor sit amet, consectetur adipisicing elit, sed do eiusmod tempor incididunt</p>
  <span class="more">READ MORE</span>
</div>
<div class="abs feature" style="left:471px">
  <div class="feature-photo" role="img" aria-label="Photo of two businessmen shaking hands against a sky" style="background:linear-gradient(180deg,#8fb0d2,#d9dde0 45%,#4a4a4c 70%,#6c6458)"></div>
  <h3>LOREM IPSUM DOLOR</h3>
  <p>Lorem ipsum dolor sit amet, consectetur adipisicing elit, sed do eiusmod tempor incididunt</p>
  <span class="more">READ MORE</span>
</div>

<section class="abs services"></section>
<h2 class="abs services-title">SERVICES</h2>
<div class="abs service" style="left:110px">
  <div class="service-photo" role="img" aria-label="Photo of a container ship at sea" style="background:linear-gradient(160deg,#6f8aa6,#b44a4a 45%,#8a9cae 75%,#5a7088)"></div>
  <span>Lorem ipsum dolor</span>
</div>
<div class="abs service" style="left:295px">
  <div class="service-photo" role="img" aria-label="Photo of a blue truck with a white trailer" style="background:linear-gradient(180deg,#dfe6ec,#b8c4cc 40%,#2c6f9c 65%,#5a5e62)"></div>
  <span>Lorem ipsum dolor</span>
</div>
<div class="abs service" style="left:478px">
  <div class="service-photo" role="img" aria-label="Photo of a passenger jet flying in a blue sky" style="background:linear-gradient(180deg,#2f6fb6,#5d95cf 50%,#a9c8e6)"></div>
  <span>Lorem ipsum dolor</span>
</div>

<h2 class="abs testi-title">TESTIMONIAL</h2>
<div class="abs avatar" role="img" aria-label="Portrait photo of the client giving the testimonial"></div>
<span class="abs qmark" style="left:172px;top:1050px">"</span>
<p class="abs quote">Lorem ipsum dolor sit amet, consectetur adipisicing elit, sed do eiusmod tempor incididunt ut labore et dolore magna aliqua. Ut enim ad minim veniam, quis nostrud exercitation ullamco laboris nisi ut aliquip ex ea commodo.</p>
<span class="abs qmark" style="left:604px;top:1066px">"</span>
<p class="abs author">Jamie Vance</p>

<footer class="abs footer-nav">
  <a class="active" style="left:134px">HOME</a>
  <a style="left:181px">ABOUT US</a>
  <a style="left:246px">SERVICES</a>
  <a style="left:314px">REQUEST A QUOTE</a>
  <a style="left:408px">OFFICE NETWORKS</a>
  <a style="left:503px">CONTACT US</a>
  <a style="left:579px">GENERAL INFO</a>
</footer>
<div class="abs footer-bar"></div>
<p class="abs copyright">COPYRIGHT © 2013 / ALL RIGHTS RESERVED</p>
<div class="abs social" style="left:567px;background:#3b5998"></div>
<div class="abs social" style="left:590px;background:#2fa9e0"></div>
<div class="abs social" style="left:614px;background:#1a6fa8"></div>
</body>
</html>
```